New Architectural Firm Business Cards

New Business card to compliment previous pixel forum logo (attached). Please design a business card that is simple, modern, creative....please do not use "symbols", simply the logo and associated graphics/text. The front should contain name/address/phone/email/web address (with graphics).....back should be 100% graphic design using the logo somehow. Hoping for a two color (black and yellow) design. full bleed design, no borders

Target Market(s)

Commercial Architecture Clients

Industry/Entity Type

Architecture

Contact Information for Business Card

Please design a business card that is simple, modern, creative....please do not use "symbols", simply the logo and associated graphics/text. The front should contain name/address/phone/email/web address (with graphics).....back should be 100% graphic design using the logo somehow

Font styles to use
Sans Serif

Colors
FFF300
FFF600
FEFA6F
FFFEC7
FFFEE8

Requirements
Must have
• Clean, Modern Design
Should not have
• Stock images or "icons"

```html
<!DOCTYPE html>
<html lang="en">
<head>
<meta charset="utf-8">
<title>Novu Architecture – Business Card</title>
<link rel="stylesheet" href="https://fonts.googleapis.com/css2?family=Poppins:wght@400;500;700;800&display=swap">
<style>
  :root {
    --bg: #3b3c3e;
    --yellow: #f2c12e;
    --yellow-light: #f6d25e;
    --ink: #1d191a;
    --paper: #ffffff;
  }
  * { margin: 0; padding: 0; box-sizing: border-box; }
  html, body { width: 1200px; height: 800px; overflow: hidden; }
  body {
    background: var(--bg);
    font-family: "Poppins", sans-serif;
    position: relative;
  }
  .card {
    position: absolute;
    top: 252px;
    width: 525px;
    height: 300px;
    overflow: hidden;
  }
  .card-front { left: 50px; background: var(--paper); }
  .card-back { left: 625px; background: var(--ink); }

  /* front */
  .front-bands { position: absolute; left: 0; top: 0; width: 525px; height: 300px; }
  .brand {
    position: absolute;
    right: 28px;
    top: 26px;
    font-weight: 700;
    font-size: 15px;
    color: var(--yellow);
    letter-spacing: 0.02em;
    display: flex;
    align-items: center;
    gap: 7px;
  }
  .brand-dot { width: 12px; height: 12px; border-radius: 50%; background: var(--yellow); }
  .person { position: absolute; left: 32px; top: 62px; }
  .person-name { font-weight: 800; font-size: 19px; color: var(--ink); letter-spacing: 0.01em; }
  .person-role { font-weight: 400; font-size: 12px; color: var(--yellow); margin-top: -2px; }
  .phones { position: absolute; left: 32px; top: 112px; font-size: 10.5px; color: var(--ink); line-height: 1.45; letter-spacing: 0.04em; }
  .details { position: absolute; left: 32px; top: 198px; color: var(--ink); font-size: 10.5px; line-height: 1.4; letter-spacing: 0.02em; }
  .details .web { margin-bottom: 10px; }
  .details strong { font-weight: 700; }

  /* back */
  .back-art { position: absolute; left: 0; top: 0; width: 525px; height: 300px; }
  .back-name {
    position: absolute;
    left: 120px;
    top: 40px;
    font-weight: 800;
    font-size: 170px;
    line-height: 1;
    color: var(--yellow);
    letter-spacing: -0.03em;
  }
</style>
</head>
<body>
  <section class="card card-front" aria-label="Business card front">
    <svg class="front-bands" viewBox="0 0 525 300" aria-hidden="true">
      <rect x="0" y="168" width="525" height="14" fill="var(--ink)"/>
      <rect x="0" y="182" width="525" height="118" fill="var(--yellow)"/>
      <path d="M0 182 L525 182 L525 168 L430 168 Q390 160 355 175 L340 182 Z" fill="var(--ink)"/>
      <path d="M340 182 Q360 150 420 160 L470 168 L470 300 L400 300 Q395 240 360 230 Z" fill="var(--yellow-light)" opacity="0.7"/>
      <path d="M360 230 Q395 240 400 300 L340 300 Z" fill="var(--ink)" opacity="0.85"/>
    </svg>
    <div class="brand"><span class="brand-dot"></span>Novu Architecture</div>
    <div class="person">
      <p class="person-name">YOUR NAME HERE</p>
      <p class="person-role">Designation here</p>
    </div>
    <div class="phones">
      <p>+ 01 555 010 482 (USA)</p>
      <p>+ 01 555 010 917 (TZ)</p>
    </div>
    <div class="details">
      <p>mara@novuarchitecture.com</p>
      <p class="web">www.novuarchitecture.com</p>
      <p><strong>Head Office:</strong> 4<sup>th</sup> Floor, Linden Court</p>
      <p>Harbor View Rd, Portland</p>
    </div>
  </section>

  <section class="card card-back" aria-label="Business card back">
    <svg class="back-art" viewBox="0 0 525 300" aria-hidden="true">
      <rect x="0" y="205" width="150" height="95" fill="var(--yellow)"/>
      <rect x="420" y="175" width="105" height="60" fill="var(--yellow)"/>
    </svg>
    <p class="back-name">novu</p>
  </section>
</body>
</html>
```